Website Landing Page Cobalt Plumbing

Dear Contestants,

I would like you to design me a landing page for my new website. I have attached a screen shot of my current website which is being constructed.

I do not want the lay out to change at all as my web designer has put this system together and the layout cannot change.

-I would like a designer to come up with something creative and appealing. I would like the website to be classy and elegant.

-I have also attached my flyer design etc so you get an idea of colours etc.

Also I have files etc of logo etc and photos if you would like me to email them that is no issue.

I am happy to provide more info if you request at anytime.

If anyone needs files I can email photos etc. Please reach out.

Plumbing

```html
<!DOCTYPE html>
<html lang="en">
<head>
<meta charset="utf-8">
<title>Cobalt Plumbing — Local Affordable Plumbing Solutions</title>
<link href="https://fonts.googleapis.com/css2?family=Montserrat:wght@400;500;600;700;800&family=Open+Sans:wght@400;600&family=Roboto+Condensed:wght@700&display=swap" rel="stylesheet">
<style>
  :root{
    --bar:#05a0c6;
    --navy:#1d4f91;
    --deep:#1a5aa3;
    --accent:#0c9fcf;
    --ink:#111;
    --muted:#333;
    --white:#fff;
    --hero-a:#1e6fd9;
    --hero-b:#d9e2ea;
  }
  *{margin:0;padding:0;box-sizing:border-box}
  html,body{width:960px;height:1200px;overflow:hidden;background:var(--white)}
  body{position:relative;font-family:"Montserrat",sans-serif;color:var(--ink)}
  .abs{position:absolute}

  .top-bar{left:0;top:0;width:960px;height:34px;background:var(--bar)}
  .social{position:absolute;top:5px;width:24px;height:24px;border-radius:50%;background:#111;border:2px solid #222}

  .brand{left:106px;top:48px;display:flex;align-items:center;gap:7px;font-weight:700;font-size:14px;color:var(--navy);letter-spacing:.2px}
  .brand-mark{width:14px;height:14px;background:var(--accent)}

  .nav{left:316px;top:73px;display:flex;gap:0;font-size:10.5px;font-weight:500;color:var(--navy)}
  .nav a{color:inherit;text-decoration:none;position:absolute;white-space:nowrap}
  .nav .active::after{content:"";position:absolute;left:0;right:0;bottom:-4px;height:2px;background:#111}
  .book-btn{left:606px;top:66px;width:78px;height:27px;background:var(--bar);color:var(--white);font-size:10.5px;font-weight:600;display:flex;align-items:center;justify-content:center}

  .phone-icon{left:748px;top:60px;width:32px;height:32px;border-radius:50%;background:#fff;box-shadow:0 2px 4px rgba(0,0,0,.18);display:flex;align-items:center;justify-content:center}
  .phone-num{left:784px;top:72px;font-size:8.5px;font-weight:600;color:var(--navy);letter-spacing:.3px}
  .phone-sub{left:784px;top:83px;font-size:5px;font-weight:700;color:#111}

  .hero{left:96px;top:108px;width:769px;height:303px;background:linear-gradient(110deg,var(--hero-a) 0%,#3d86e0 28%,#c9d6e2 42%,var(--hero-b) 100%)}
  .hero-line1{left:398px;top:196px;font-size:24px;font-weight:800;color:var(--navy);letter-spacing:1.6px}
  .hero-line2{left:493px;top:233px;font-size:24px;font-weight:800;color:var(--accent);letter-spacing:1.6px}
  .learn-btn{left:470px;top:298px;width:160px;height:33px;background:var(--white);color:var(--accent);font-size:14px;font-weight:800;letter-spacing:.8px;display:flex;align-items:center;justify-content:center}
  .dot{position:absolute;border-radius:50%;background:#fff}

  .tagline{left:0;top:442px;width:960px;text-align:center;font-size:24px;font-weight:800;letter-spacing:1.5px;color:var(--deep)}
  .tagline span{color:var(--accent)}
  .intro{left:0;width:960px;text-align:center;font-size:10.5px;letter-spacing:.4px;color:var(--ink)}

  .section-title{font-size:19px;font-weight:700;letter-spacing:1.2px;color:var(--ink);white-space:nowrap}
  .section-title span{color:var(--accent)}
  .rule{height:2px;background:var(--deep)}

  .feature-icon{position:absolute;width:36px;height:50px;border-radius:50%;background:#fff;box-shadow:-2px 0 4px rgba(0,0,0,.2);display:flex;align-items:center;justify-content:center}
  .feature-title{position:absolute;font-family:"Roboto Condensed",sans-serif;font-weight:700;font-size:14px;color:var(--deep);letter-spacing:.2px}
  .feature-text{position:absolute;font-family:"Open Sans",sans-serif;font-size:8.5px;line-height:13.6px;color:#222;width:150px}

  .worker{left:96px;top:768px;width:96px;height:268px;background:linear-gradient(180deg,#c8633f 0%,#a44a55 25%,#2b4fc4 45%,#1f3fb0 85%,#333 100%);border-radius:40px 40px 6px 6px}

  .service-list{left:227px;top:856px;list-style:none}
  .service-list li{position:relative;height:24px;padding-left:18px;font-size:11px;font-weight:700;letter-spacing:.5px;color:#111;display:flex;align-items:center}
  .service-list svg{position:absolute;left:0;top:5px}

  .lowcost-title{left:503px;top:788px;width:370px;text-align:center;font-size:19px;font-weight:700;letter-spacing:1.2px;line-height:24px;color:var(--ink)}
  .lowcost-title span{color:var(--accent)}
  .lowcost-copy{left:503px;width:356px;font-size:10.5px;line-height:18.5px;letter-spacing:.5px;color:#111}
  .see-btn{left:622px;top:1009px;width:123px;height:28px;border:1.5px solid var(--deep);color:var(--navy);font-size:11px;font-weight:700;letter-spacing:.5px;display:flex;align-items:center;justify-content:center}

  .footer{left:0;top:1124px;width:960px;height:76px;background:var(--bar)}
  .footer a{position:absolute;top:29px;font-size:10.5px;font-weight:700;color:var(--white);text-decoration:none;white-space:nowrap}
</style>
</head>
<body>

<div class="abs top-bar">
  <span class="social" style="left:748px"></span>
  <span class="social" style="left:777px"></span>
  <span class="social" style="left:806px"></span>
  <span class="social" style="left:835px"></span>
</div>

<div class="abs brand"><span class="brand-mark"></span>Cobalt Plumbing</div>

<nav class="abs nav">
  <a class="active" style="left:0">HOME</a>
  <a style="left:53px">SERVICES</a>
  <a style="left:127px">ABOUT US</a>
  <a style="left:206px">CONTACT US</a>
</nav>
<div class="abs book-btn">BOOK NOW</div>

<div class="abs phone-icon">
  <svg width="16" height="16" viewBox="0 0 24 24" fill="none" stroke="#1d6fb8" stroke-width="1.6"><path d="M5 3h4l2 5-3 2a12 12 0 0 0 6 6l2-3 5 2v4a2 2 0 0 1-2 2A17 17 0 0 1 3 5a2 2 0 0 1 2-2z"/></svg>
</div>
<div class="abs phone-num">1300-555-018</div>
<div class="abs phone-sub">24*7 CUSTOMER CARE</div>

<section class="abs hero" role="img" aria-label="Flat lay of plumbing fittings, tap, hoses and wrench on blue and white surface"></section>
<h1 class="abs hero-line1">LOCAL AFFORDABLE</h1>
<div class="abs hero-line2">PLUMBING SOLUTIONS</div>
<div class="abs learn-btn">LEARN MORE</div>
<span class="dot" style="left:453px;top:374px;width:10px;height:10px"></span>
<span class="dot" style="left:470px;top:370px;width:18px;height:18px;background:#1e8fe6"></span>
<span class="dot" style="left:496px;top:374px;width:10px;height:10px"></span>

<h2 class="abs tagline">TWICE THE QUALITY <span>TWICE THE SERVICE</span></h2>
<p class="abs intro" style="top:482px">Lorem ipsum dolor sit amet, consectetur adipisicing elit, sed do eiusmod tempor</p>
<p class="abs intro" style="top:504px">incididunt ut labore et dolore magna aliqua. Ut enim ad minim veniam, quis nostrud exercitation ullamco laboris nisi</p>

<h2 class="abs section-title" style="left:392px;top:557px">OUR <span>FEATURES</span></h2>
<div class="abs rule" style="left:455px;top:586px;width:49px"></div>

<div class="feature-icon" style="left:96px;top:612px">
  <svg width="14" height="22" viewBox="0 0 14 22" fill="none" stroke="#2a9fd0" stroke-width="1.6"><path d="M1 1h12M1 21h12M2 1c0 6 10 6 10 10S2 15 2 21M12 1c0 6-10 6-10 10s10 4 10 10"/></svg>
</div>
<div class="feature-title" style="left:136px;top:612px">EFFICIENT</div>
<p class="feature-text" style="left:137px;top:636px">We won't waste your time we pride ourselves on solving your problem</p>

<div class="feature-icon" style="left:300px;top:608px">
  <svg width="18" height="18" viewBox="0 0 24 24" fill="#2a9fd0"><path d="M21 6a5 5 0 0 1-6.6 4.7L6 19a2 2 0 1 1-3-3l8.3-8.4A5 5 0 0 1 18 2l-3 3 1 3 3 1z"/></svg>
</div>
<div class="feature-title" style="left:344px;top:609px">RELIABLE</div>
<p class="feature-text" style="left:345px;top:631px">We arrive on time and come pre-pared our vans are stocked to handle your issue.</p>

<div class="feature-icon" style="left:502px;top:614px">
  <svg width="12" height="22" viewBox="0 0 12 22"><text x="0" y="18" font-family="Montserrat,sans-serif" font-size="20" fill="#2a9fd0">$</text></svg>
</div>
<div class="feature-title" style="left:543px;top:612px">RESPECTFULL</div>
<p class="feature-text" style="left:544px;top:636px">We value our customers and treat them with respect we'll always leave your home tidy.</p>

<div class="feature-icon" style="left:705px;top:614px">
  <svg width="18" height="20" viewBox="0 0 18 20" fill="#2a9fd0"><circle cx="9" cy="4" r="3"/><rect x="3" y="8" width="12" height="10" rx="2"/></svg>
</div>
<div class="feature-title" style="left:746px;top:612px">AFFORDABLE</div>
<p class="feature-text" style="left:748px;top:636px">We pice competitively and never overcharge.our billing process is transparent.</p>

<div class="abs worker" role="img" aria-label="Plumber in blue overalls and hard hat holding a toolbox and wrench"></div>

<h2 class="abs section-title" style="left:226px;top:783px">OUR <span>SEVICES</span></h2>
<div class="abs rule" style="left:273px;top:811px;width:49px"></div>

<ul class="abs service-list">
  <li><svg width="9" height="13" viewBox="0 0 9 13"><path d="M4.5 0C3 4 0 6 0 8.5a4.5 4.5 0 0 0 9 0C9 6 6 4 4.5 0z" fill="#1e8fe6"/></svg>Same Day Service</li>
  <li><svg width="9" height="13" viewBox="0 0 9 13"><path d="M4.5 0C3 4 0 6 0 8.5a4.5 4.5 0 0 0 9 0C9 6 6 4 4.5 0z" fill="#1e8fe6"/></svg>Blocked Drains</li>
  <li><svg width="9" height="13" viewBox="0 0 9 13"><path d="M4.5 0C3 4 0 6 0 8.5a4.5 4.5 0 0 0 9 0C9 6 6 4 4.5 0z" fill="#1e8fe6"/></svg>Hot Water</li>
  <li><svg width="9" height="13" viewBox="0 0 9 13"><path d="M4.5 0C3 4 0 6 0 8.5a4.5 4.5 0 0 0 9 0C9 6 6 4 4.5 0z" fill="#1e8fe6"/></svg>Burst pipe,Leakingtaps &amp; Toilets</li>
  <li><svg width="9" height="13" viewBox="0 0 9 13"><path d="M4.5 0C3 4 0 6 0 8.5a4.5 4.5 0 0 0 9 0C9 6 6 4 4.5 0z" fill="#1e8fe6"/></svg>Gas Installations</li>
  <li><svg width="9" height="13" viewBox="0 0 9 13"><path d="M4.5 0C3 4 0 6 0 8.5a4.5 4.5 0 0 0 9 0C9 6 6 4 4.5 0z" fill="#1e8fe6"/></svg>Leak Detection</li>
  <li><svg width="9" height="13" viewBox="0 0 9 13"><path d="M4.5 0C3 4 0 6 0 8.5a4.5 4.5 0 0 0 9 0C9 6 6 4 4.5 0z" fill="#1e8fe6"/></svg>Emergency Service</li>
</ul>

<h2 class="abs lowcost-title">EVERYDAY <span>LOWCOST<br>PLUMBING</span></h2>
<p class="abs lowcost-copy" style="top:842px">Lorem ipsum dolor sit amet, csectetur adipisicing elit, sed do eiu mod tempor incididunt ut labore et dolore magna aliqua.</p>
<p class="abs lowcost-copy" style="top:916px">Ut enim ad minim veniam, quis nostrud exercitation ul-lamco laboris nisiutaliquip ex ea commodo. consequat. &nbsp;Duis aute irure dolor in reprehenderit in voluptate velit esse cillum dolore eu fugiat nulla pariatur. Excepteur</p>
<div class="abs see-btn">SEE MORE</div>

<footer class="abs footer">
  <a style="left:302px">HOME</a>
  <a style="left:355px">SERVICES</a>
  <a style="left:429px">ABOUT US</a>
  <a style="left:508px">CONTACT US</a>
  <a style="left:598px">BOOK NOW</a>
</footer>

</body>
</html>
```